Launch of a new Investment fund

Im looking for someone design a logo and website for my Investment fund located in Singapore.

Attached to this project you will find a project scope document that details exactly what i am looking for and also includes a website copy that i have written up. I am happy for you to take your own inspiration as well to design the website. At this stage the website wont be very detailed as there isn't much information to showcase. I will require the website to be easily editable in the future so i can update it with progress the fund makes.

If you require any further details on the project please reach out to me

Coding

Coded - Design and coding required

Number of Pages Required

4 page

```html
<!DOCTYPE html>
<html lang="en">
<head>
<meta charset="utf-8">
<title>Northquay Capital Management</title>
<link href="https://fonts.googleapis.com/css2?family=Jost:wght@400;500;600&family=League+Spartan:wght@700&display=swap" rel="stylesheet">
<style>
:root{
  --ink:#111320;
  --white:#ffffff;
  --blue:#3366f0;
  --blue-bright:#3b6cff;
  --navy-deep:#0d0d1c;
  --bar:#233b82;
  --muted:#d8dbe6;
  --line:#e4e6ee;
  --hero-a:#2a2f45;
  --hero-b:#17204a;
}
*{box-sizing:border-box;margin:0;padding:0}
html,body{width:1200px;height:937px;overflow:hidden}
body{position:relative;font-family:"Jost",sans-serif;color:var(--ink);background:var(--white)}

.site-header{position:absolute;left:0;top:0;width:1200px;height:77px;background:var(--white)}
.brand{position:absolute;left:154px;top:22px;display:flex;align-items:center;gap:8px}
.brand-dot{width:30px;height:30px;border-radius:50%;background:var(--blue)}
.brand-name{font-family:"Jost",sans-serif;font-weight:600;font-size:15px;line-height:15px;letter-spacing:.5px;color:var(--ink)}
.brand-name small{display:block;font-size:15px;font-weight:600}
.main-nav{position:absolute;left:476px;top:32px;display:flex;gap:24px;font-size:11px;font-weight:500;letter-spacing:.4px}
.main-nav a{color:var(--ink);text-decoration:none}
.main-nav a.active{color:var(--blue);border-bottom:1px solid var(--blue)}
.header-divider{position:absolute;top:0;width:1px;height:77px;background:var(--line)}
.social{display:flex;gap:10px}
.social span{width:14px;height:14px;border-radius:50%;border:1.5px solid currentColor}
.header-social{position:absolute;left:829px;top:32px;color:var(--ink)}
.help{position:absolute;left:899px;top:26px;display:flex;gap:7px;align-items:center}
.help-icon{width:25px;height:25px;border-radius:50%;background:var(--blue);display:flex;align-items:center;justify-content:center}
.help p{font-size:9px;line-height:12px}
.help strong{font-size:11.5px;font-weight:500;letter-spacing:.4px}

.hero{position:absolute;left:0;top:77px;width:1200px;height:565px;overflow:hidden;
  background:linear-gradient(100deg,var(--hero-a) 0%,#262a3e 40%,var(--hero-b) 100%)}
.hero svg{position:absolute;left:0;top:0}
.hero-title{position:absolute;left:149px;top:209px;font-family:"League Spartan",sans-serif;font-weight:700;font-size:45px;line-height:50px;color:var(--white);letter-spacing:.3px}

.site-footer{position:absolute;left:0;top:642px;width:1200px;height:257px;background:var(--navy-deep);color:var(--muted)}
.footer-brand{position:absolute;left:151px;top:80px;width:151px;text-align:center}
.footer-brand .brand-dot{margin:0 auto 10px;width:44px;height:44px}
.footer-brand .brand-name{color:var(--muted);font-size:18px;line-height:20px}
.footer-brand .brand-name small{font-size:18px}
.col-title{font-family:"League Spartan",sans-serif;font-weight:700;font-size:14px;letter-spacing:.6px;color:var(--blue-bright);margin-bottom:12px}
.col{position:absolute;top:57px;font-size:11px;line-height:18px}
.contact{left:392px}
.contact li{list-style:none;display:flex;gap:9px;margin-bottom:11px}
.contact svg{flex:none;margin-top:3px}
.links{left:652px}
.links li{list-style:none;margin-bottom:4px}
.links a{color:var(--muted);text-decoration:none}
.links a.active{color:var(--blue);text-decoration:underline}
.newsletter{left:812px;width:240px}
.newsletter p{font-size:11px;line-height:16px;margin-bottom:13px}
.email-field{display:block;width:238px;height:32px;border:1px solid #3a3c4e;background:transparent;color:#9a9db0;font:400 10.5px "Jost",sans-serif;padding-left:19px;line-height:30px}
.subscribe{display:block;margin-top:12px;width:122px;height:34px;background:var(--blue-bright);color:var(--white);font:600 10px "Jost",sans-serif;letter-spacing:.4px;text-align:center;line-height:34px}

.bottom-bar{position:absolute;left:0;top:899px;width:1200px;height:38px;background:var(--bar);color:var(--muted)}
.bottom-bar p{position:absolute;left:149px;top:11px;font-size:11px}
.bottom-social{position:absolute;left:1005px;top:12px;color:var(--muted)}
</style>
</head>
<body>
<header class="site-header">
  <div class="brand"><span class="brand-dot"></span><div class="brand-name">NORTHQUAY CAPITAL<small>MANAGEMENT</small></div></div>
  <nav class="main-nav">
    <a class="active" href="#">HOME</a><a href="#">ABOUT US</a><a href="#">INVESTMENTS</a><a href="#">CONTACT US</a>
  </nav>
  <span class="header-divider" style="left:811px"></span>
  <span class="header-divider" style="left:886px"></span>
  <div class="social header-social"><span></span><span></span></div>
  <div class="help">
    <span class="help-icon"><svg width="12" height="12" viewBox="0 0 24 24"><path d="M6.6 10.8a15 15 0 0 0 6.6 6.6l2.2-2.2a1 1 0 0 1 1-.25 11 11 0 0 0 3.6.6 1 1 0 0 1 1 1V20a1 1 0 0 1-1 1A17 17 0 0 1 3 4a1 1 0 0 1 1-1h3.5a1 1 0 0 1 1 1 11 11 0 0 0 .6 3.6 1 1 0 0 1-.25 1z" fill="none" stroke="#fff" stroke-width="1.8"/></svg></span>
    <p>Need help? Talk to an expert<br><strong>+1 555 010 2748</strong></p>
  </div>
</header>

<section class="hero" role="img" aria-label="Photo of an analyst studying market charts on a screen">
  <svg width="1200" height="565" viewBox="0 0 1200 565">
    <polygon points="677,0 795,0 1136,565 1020,565" fill="#8fa0d8" opacity=".18"/>
    <polygon points="960,0 1165,0 1200,0 1200,565 746,565" fill="#1d3fb0" opacity=".35"/>
    <polygon points="898,360 1136,565 746,565" fill="#2a52e0" opacity=".35"/>
  </svg>
  <h1 class="hero-title">PASSION FOR<br>UNCOVERING NEW<br>OPPORTUNITIES</h1>
</section>

<footer class="site-footer">
  <div class="footer-brand"><span class="brand-dot"></span><div class="brand-name">NORTHQUAY CAPITAL<small>MANAGEMENT</small></div></div>
  <div class="col contact">
    <h2 class="col-title">CONATCT INFO</h2>
    <ul>
      <li><svg width="12" height="14" viewBox="0 0 12 14"><path d="M6 0a5 5 0 0 1 5 5c0 4-5 9-5 9S1 9 1 5a5 5 0 0 1 5-5z" fill="#3b6cff"/><circle cx="6" cy="5" r="2" fill="#0d0d1c"/></svg><span>214 Marlow Ridge Ln.,<br>Alder, CA95310</span></li>
      <li><svg width="12" height="12" viewBox="0 0 24 24"><path d="M6.6 10.8a15 15 0 0 0 6.6 6.6l2.2-2.2a1 1 0 0 1 1-.25 11 11 0 0 0 3.6.6 1 1 0 0 1 1 1V20a1 1 0 0 1-1 1A17 17 0 0 1 3 4a1 1 0 0 1 1-1h3.5a1 1 0 0 1 1 1 11 11 0 0 0 .6 3.6 1 1 0 0 1-.25 1z" fill="#3b6cff"/></svg><span>+1 555 010 2748</span></li>
      <li><svg width="13" height="10" viewBox="0 0 13 10"><rect width="13" height="10" fill="#3b6cff"/><path d="M0 0l6.5 5L13 0" stroke="#0d0d1c" fill="none"/></svg><span>info@northquaycapital.com</span></li>
      <li><svg width="13" height="13" viewBox="0 0 13 13"><circle cx="6.5" cy="6.5" r="6" fill="#3b6cff"/><path d="M0.5 6.5h12M6.5 0.5v12" stroke="#0d0d1c"/></svg><span>Live location</span></li>
    </ul>
  </div>
  <div class="col links">
    <h2 class="col-title">QUICK LINK</h2>
    <ul>
      <li><a class="active" href="#">Home</a></li><li><a href="#">About Us</a></li><li><a href="#">Investments</a></li>
      <li><a href="#">Contact Us</a></li><li><a href="#">Terms of Use</a></li><li><a href="#">Privacy Policy</a></li>
    </ul>
  </div>
  <div class="col newsletter">
    <h2 class="col-title">STAY IN TOUCH</h2>
    <p>Subscribe to our newsletter and<br>stay updated</p>
    <span class="email-field">Your email address*</span>
    <span class="subscribe">SUBSCRIBE NOW</span>
  </div>
</footer>

<div class="bottom-bar">
  <p>© 2024 Northquay Capital Management. All Right Reserved</p>
  <div class="social bottom-social"><span></span><span></span></div>
</div>
</body>
</html>
```